The most amazing design opportunity you will ever get - Plus we may even through in some shares!

We need a new look and feel for our website, something that will knock the socks off our competitors. Something fresh, functional, dynamic and awesome.

Take a look at the attached brief and see if this is something you can get you head around to come up with something just amazing.

A key to your success is to base your design on the Visual Language (colours Black with Orange on white background, integration of cogs, font, style) and remember that our target audience is BUSINESS and the key thing that we are about is INSIGHTS, so if you can include some subtle design that requires insight to use - Perfect!

```html
<!DOCTYPE html>
<html lang="en">
<head>
<meta charset="utf-8">
<title>Keystone Business Insights</title>
<link rel="stylesheet" href="https://fonts.googleapis.com/css2?family=Titillium+Web:wght@300;400;600;700&family=Arimo:wght@400;700&family=Tinos:ital@1&display=swap">
<style>
:root{
  --orange:#ff8533;
  --orange-deep:#ff6600;
  --orange-soft:#ff8c42;
  --gold:#ffc21f;
  --ink:#111;
  --text:#7a7a7a;
  --text-strong:#555;
  --link:#f07a2a;
  --panel:#dcdcdc;
  --tab:#e8e8e8;
  --btn:#808080;
  --line:#c9c9c9;
}
*{box-sizing:border-box;margin:0;padding:0}
html,body{width:1200px;height:1098px;overflow:hidden;background:#fff}
body{position:relative;font-family:Arimo,Arial,sans-serif;color:var(--ink)}
.abs{position:absolute}

/* status bar */
.status-bar{left:0;top:0;width:1200px;height:120px;background:linear-gradient(#fafafa,#e2e2e2);border-bottom:2px solid #cfcfcf}
.status-bar .icon{left:39px;top:36px}
.status-title{left:104px;top:44px;font-weight:700;font-size:26px;letter-spacing:.5px}
.stats-box{left:293px;top:39px;width:875px;height:39px;background:#fff;border:2px solid #bdbdbd;border-radius:3px;box-shadow:inset 0 2px 3px rgba(0,0,0,.15)}
.stat{top:50px;font-size:15px;color:var(--ink)}
.stat-label{top:89px;font-size:12.5px;color:#8a8a8a}
.divider{top:0;width:1px;height:120px;background:#c4c4c4;box-shadow:1px 0 0 #fff}

/* header */
.brand{left:34px;top:138px;font-family:"Titillium Web",sans-serif;font-weight:700;font-size:56px;line-height:1;color:var(--ink)}
.brand-tagline{left:234px;top:134px;font-family:Arimo,Arial,sans-serif;font-size:19px;line-height:24px;color:var(--ink)}
.notice{left:610px;top:147px;font-weight:700;font-size:19px;line-height:23px}
.notice .lead{font-size:20px}
.up-btn{left:1117px;top:183px}

/* orange band */
.band{left:0;top:237px;width:1200px;height:253px;background:var(--orange)}
.insights-bar{left:24px;top:271px;width:1146px;height:73px;background:var(--orange-soft);border:1px solid #ffb060;box-shadow:0 10px 10px -6px rgba(0,0,0,.45)}
.insights-bar .icon{left:18px;top:12px}
.insights-title{left:76px;top:21px;font-weight:700;font-size:25px;color:var(--gold);letter-spacing:.5px}
.insights-slogan{right:24px;top:20px;font-family:Tinos,"Times New Roman",serif;font-style:italic;font-size:25px;color:var(--ink)}
.main-nav{left:24px;top:380px;width:1146px;height:76px;background:var(--orange-deep);border:1px solid #e0a000}
.main-nav a{position:absolute;top:25px;font-size:19px;color:var(--ink);text-decoration:none}
.main-nav a.current{color:var(--gold)}

/* intro */
.intro-title{left:39px;top:537px;font-family:"Titillium Web",sans-serif;font-weight:400;font-size:40px;color:#333}
.intro-copy{left:39px;top:608px;width:740px;font-family:"Titillium Web",sans-serif;font-weight:400;font-size:20px;line-height:34.6px;color:var(--text)}
.intro-copy b{font-weight:700;color:var(--text-strong)}
.intro-copy .accent{color:var(--link)}

/* login panel */
.side-panel{left:777px;top:490px;width:423px;height:608px;background:var(--panel)}
.login-card{left:815px;top:490px;width:355px;height:550px;background:#fff}
.tabs{left:815px;top:490px;width:355px;height:60px}
.tab{position:absolute;top:0;height:60px;line-height:58px;font-size:15px;text-align:center;color:#777}
.tab.active{left:0;width:114px;background:#fff;color:var(--ink)}
.tab-rest{position:absolute;left:114px;top:0;width:241px;height:60px;background:var(--tab)}
.field{left:858px;width:269px;height:33px;border:1px solid var(--line);background:#fff}
.remember{left:858px;top:735px;font-size:15px;display:flex;align-items:center;gap:8px}
.remember span.box{width:17px;height:17px;border:1px solid #333;margin-top:-6px}
.sum-note{left:860px;top:779px;font-size:14.5px}
.captcha{left:858px;top:805px;width:269px;height:61px;background:var(--panel)}
.captcha .q{position:absolute;left:14px;top:20px;font-weight:700;font-size:18px;color:#888}
.captcha .ans{position:absolute;left:103px;top:15px;width:85px;height:34px;border:1px solid #c8c8c8;background:#ddd}
.login-btn{left:858px;top:874px;width:269px;height:51px;background:var(--btn);color:#fff;font-weight:700;font-size:19px;text-align:center;line-height:51px}
</style>
</head>
<body>

<header class="status-bar abs">
  <svg class="icon abs" width="48" height="48" viewBox="0 0 48 48" aria-hidden="true">
    <circle cx="24" cy="24" r="22" fill="#fff" stroke="#555" stroke-width="3"/>
    <circle cx="24" cy="24" r="17" fill="#eee" stroke="#ccc"/>
    <path d="M19 15 L32 24 L19 33 Z" fill="#333"/>
  </svg>
  <div class="status-title abs">JUST ME</div>
  <div class="stats-box abs"></div>
  <div class="divider abs" style="left:430px"></div>
  <div class="divider abs" style="left:550px"></div>
  <div class="divider abs" style="left:669px"></div>
  <div class="divider abs" style="left:789px"></div>
  <div class="divider abs" style="left:908px"></div>
  <div class="divider abs" style="left:1028px"></div>
  <div class="stat abs" style="left:310px">1</div>
  <div class="stat abs" style="left:434px">15,200</div>
  <div class="stat abs" style="left:552px">7,500</div>
  <div class="stat abs" style="left:671px">4,380</div>
  <div class="stat abs" style="left:790px">3,120</div>
  <div class="stat abs" style="left:910px">7,700</div>
  <div class="stat abs" style="left:1030px">5,000</div>
  <div class="stat-label abs" style="left:310px">Me</div>
  <div class="stat-label abs" style="left:437px">My Points</div>
  <div class="stat-label abs" style="left:557px">My Attributes</div>
  <div class="stat-label abs" style="left:676px">My Activity</div>
  <div class="stat-label abs" style="left:796px">My Networking</div>
  <div class="stat-label abs" style="left:915px">My Dollars</div>
  <div class="stat-label abs" style="left:1036px">My Shares</div>
</header>

<div class="brand abs">KEYSTONE</div>
<div class="brand-tagline abs" style="left:312px">BUSINESS<br>SOLUTIONS<br>THROUGH<br>INSIGHT</div>
<div class="notice abs"><div class="lead">NOTICE BOARD</div>Promotions<br>etc.</div>
<svg class="up-btn abs" width="48" height="48" viewBox="0 0 48 48" aria-hidden="true">
  <circle cx="24" cy="24" r="22" fill="#fff" stroke="#555" stroke-width="3"/>
  <circle cx="24" cy="24" r="17" fill="#eee" stroke="#ccc"/>
  <path d="M15 30 L24 17 L33 30 Z" fill="#fff" stroke="#777" stroke-width="2"/>
</svg>

<section class="band abs">
</section>
<div class="insights-bar abs">
  <svg class="icon abs" width="48" height="48" viewBox="0 0 48 48" aria-hidden="true">
    <circle cx="24" cy="24" r="22" fill="#fff" stroke="#555" stroke-width="3"/>
    <circle cx="24" cy="24" r="17" fill="#eee" stroke="#ccc"/>
    <path d="M14 18 L34 18 L24 33 Z" fill="#ff6600"/>
  </svg>
  <div class="insights-title abs">INSIGHTS</div>
  <div class="insights-slogan abs">We will help you see deeper</div>
</div>
<nav class="main-nav abs">
  <a class="current" style="left:15px">HOME</a>
  <a style="left:119px">DISCIPLINES</a>
  <a style="left:282px">INSIGHTS</a>
  <a style="left:416px">LIBRARY</a>
  <a style="left:541px">REWARDS</a>
  <a style="left:691px">MEMBERS</a>
  <a style="left:835px">HIRE ME</a>
  <a style="left:959px">ABOUT US</a>
</nav>

<h1 class="intro-title abs">Why Keystone Business Insights</h1>
<p class="intro-copy abs">We are dedicated to helping you solve business problems holistically, <b>self-serve</b> or with the <b>help of a specialist</b>. A single portal where you can access <b>solutions</b> and <b>insights</b> across <b>20 business disciplines</b>. <span class="accent">Become a member</span>, share your experiences with others, earn points for your <span class="accent">participation</span> and get recognized as a trusted advisor in the global community. Start out as a Newbie, then quickly climb the ranks from <b>One Star</b> Intermediate, through to a <b>Five Star</b> Guru.</p>

<aside class="side-panel abs"></aside>
<div class="login-card abs"></div>
<div class="tabs abs">
  <div class="tab-rest"></div>
  <div class="tab active">Login</div>
  <div class="tab" style="left:114px;width:120px">Register</div>
  <div class="tab" style="left:234px;width:121px">Forgot</div>
</div>
<div class="field abs" style="top:655px"></div>
<div class="field abs" style="top:687px"></div>
<div class="remember abs"><span class="box"></span>Remember Me</div>
<div class="sum-note abs">Please solve this sum to sign in</div>
<div class="captcha abs"><span class="q">9 - five =</span><span class="ans"></span></div>
<div class="login-btn abs">LOGIN</div>

</body>
</html>
```